Business Cards for a unique Russian patisserie

VOLTA Russian Treats bakery intends to introduce Australian public to amazing Russian pastries and traditions of genuine Russian hospitality.
VOLTA business model is a café, selling a mix of Russian, Eastern European and traditional pastries produced in-house.
VOLTA’s ultimate goal is to create a superior eating experience and to become a destination eatery in Sydney.
I would like the business cards match our ambitious purpose, to be unique and bold. I want them to be sophisticated (as opposed to straightforward and tacky) and graphical. I would love if Russian national ornament (hohloma) elements to be used.
Dominating colours - red and black. For the styling guide please see our logo attached.
Target Market(s)
Business partners, suppliers, possible corporate clients
Industry/Entity Type
Bakery

```html
<!DOCTYPE html>
<html lang="en">
<head>
<meta charset="utf-8">
<title>VOLTA Russian Treats – Business Cards</title>
<link rel="stylesheet" href="https://fonts.googleapis.com/css2?family=Open+Sans:wght@400;600;700&display=swap">
<style>
  :root {
    --stage: #e9e4de;
    --card-light: #ffffff;
    --card-dark: #3a2616;
    --brand-red: #e2222b;
    --brand-brown: #3a2616;
    --ink: #231f20;
    --rule: #9a9a9a;
    --on-dark: #ffffff;
  }
  * { margin: 0; padding: 0; box-sizing: border-box; }
  html, body {
    width: 1200px;
    height: 1152px;
    overflow: hidden;
    background: var(--stage);
    font-family: "Open Sans", Arial, sans-serif;
  }
  .card {
    position: absolute;
    width: 906px;
    height: 516px;
    box-shadow: 0 2px 6px rgba(0,0,0,0.25);
  }
  .card--front { left: 23px; top: 39px; background: var(--card-light); border: 1px solid #6e6e6e; }
  .card--back  { left: 272px; top: 590px; background: var(--card-dark); }

  /* front: brand block */
  .brand {
    position: absolute;
    left: 90px;
    top: 60px;
    width: 360px;
    display: flex;
    flex-direction: column;
    align-items: center;
  }
  .brand__dot {
    width: 180px;
    height: 180px;
    border-radius: 50%;
    background: var(--brand-red);
  }
  .brand__name {
    margin-top: 34px;
    color: var(--brand-brown);
    font-weight: 700;
    text-align: center;
    line-height: 1;
  }
  .brand__name-main { display: block; font-size: 74px; letter-spacing: 2px; }
  .brand__name-sub  { display: block; font-size: 20px; margin-top: 10px; }

  .divider {
    position: absolute;
    left: 497px;
    top: 86px;
    width: 2px;
    height: 336px;
    background: var(--rule);
  }

  /* front: contact block */
  .contact {
    position: absolute;
    left: 521px;
    top: 90px;
    color: var(--ink);
  }
  .contact__name  { color: var(--brand-red); font-size: 30px; font-weight: 700; line-height: 36px; }
  .contact__title { font-size: 22px; line-height: 30px; margin-bottom: 26px; }
  .contact__list  { list-style: none; }
  .contact__item  {
    display: flex;
    align-items: center;
    gap: 10px;
    font-size: 22px;
    line-height: 36px;
  }
  .contact__icon  { width: 18px; height: 18px; flex: none; fill: var(--brand-red); }
  .contact__address { margin-top: 34px; font-size: 20px; line-height: 32px; }

  /* back */
  .back-brand {
    position: absolute;
    left: 0;
    top: 46px;
    width: 100%;
    display: flex;
    flex-direction: column;
    align-items: center;
  }
  .back-brand__dot {
    width: 230px;
    height: 230px;
    border-radius: 50%;
    background: var(--brand-red);
  }
  .back-brand__name {
    margin-top: 36px;
    color: var(--on-dark);
    font-weight: 700;
    text-align: center;
    line-height: 1;
  }
  .back-brand__name-main { display: block; font-size: 52px; letter-spacing: 3px; }
  .back-brand__name-sub  { display: block; font-size: 18px; margin-top: 8px; }
  .back-url {
    position: absolute;
    left: 0;
    bottom: 48px;
    width: 100%;
    text-align: center;
    color: var(--on-dark);
    font-size: 26px;
    letter-spacing: 5px;
  }
</style>
</head>
<body>

<section class="card card--front">
  <div class="brand">
    <div class="brand__dot"></div>
    <p class="brand__name">
      <span class="brand__name-main">VOLTA</span>
      <span class="brand__name-sub">Russian Treats</span>
    </p>
  </div>

  <div class="divider"></div>

  <div class="contact">
    <p class="contact__name">Your Name</p>
    <p class="contact__title">Title</p>
    <ul class="contact__list">
      <li class="contact__item">
        <svg class="contact__icon" viewBox="0 0 20 20"><path d="M5 1l3 4-2 2c1 3 4 6 7 7l2-2 4 3-2 4C8 19 1 12 1 3z"/></svg>
        012-345-6789
      </li>
      <li class="contact__item">
        <svg class="contact__icon" viewBox="0 0 20 20"><path d="M4 4h12l2 6v6h-3v-2H5v2H2v-6zM5 6l-1 4h12l-1-4z"/></svg>
        012-345-6789
      </li>
      <li class="contact__item">
        <svg class="contact__icon" viewBox="0 0 20 20"><path d="M1 4h18v12H1zM3 6v1l7 5 7-5V6l-7 5z"/></svg>
        info@voltatreats.com
      </li>
      <li class="contact__item">
        <svg class="contact__icon" viewBox="0 0 20 20"><path d="M10 1a9 9 0 100 18 9 9 0 000-18zm0 2c1.5 1.5 2.5 4 2.5 7s-1 5.5-2.5 7c-1.5-1.5-2.5-4-2.5-7s1-5.5 2.5-7zM3 9h14v2H3z"/></svg>
        www.voltatreats.com
      </li>
    </ul>
    <p class="contact__address">Street Name, City Name<br>Zip Code-00000</p>
  </div>
</section>

<section class="card card--back">
  <div class="back-brand">
    <div class="back-brand__dot"></div>
    <p class="back-brand__name">
      <span class="back-brand__name-main">VOLTA</span>
      <span class="back-brand__name-sub">Russian Treats</span>
    </p>
  </div>
  <p class="back-url">www.voltatreats.com</p>
</section>

</body>
</html>
```